Bright, Bold Sydney Tutoring Business Flyer Advertisment

Lumivora is an up and coming tutoring business located on Sydney's Upper North Shore catering to school students of all ages. We need a flyer designed for notice boards and letter box drops to attract new clients. Our tutors are mostly university education students who are fresh, dedicated and passionate about their areas of teaching. The flyer should exhibit a bright, bold, modern, clean cut style which would appeal to both students and parents. I have attached our logo (the flyer could reflect this colour scheme), and a PDF which outlines the information we would like to appear on the flyer. This is not set in stone, but designed to act as an extremely loose guide for your creativity !

Target Market(s)

Affluent School Students and Parents

Industry/Entity Type

Tutoring

Requirements
Must have
• Logo, $10 offer, company description.
Nice to have
• Grabbing headlines to attract new clients, such as "Feeling overwhelmed at school?". We are looking for an eye catching, clean cut and professional design that has the colours to attract kids and the tone to attract parents.

```html
<!DOCTYPE html>
<html lang="en">
<head>
<meta charset="utf-8">
<title>Lumivora Tutoring Flyer</title>
<link rel="stylesheet" href="https://fonts.googleapis.com/css2?family=Cabin+Sketch:wght@400;700&family=Questrial&family=Arvo:wght@400;700&display=swap">
<style>
  :root {
    --backdrop: #e4e3e8;
    --paper: #ffffff;
    --ink: #1a1a1a;
    --logo-ink: #3a3a3a;
    --board: #38393b;
    --board-frame: #a9774a;
    --chalk-pink: #f2a3b3;
    --chalk-blue: #8fd0f2;
    --chalk-green: #d6ea86;
    --offer-pink: #ea6b9c;
    --footer-blue: #4a9fd8;
    --white: #ffffff;
  }
  * { margin: 0; padding: 0; box-sizing: border-box; }
  html, body {
    width: 969px; height: 1200px; overflow: hidden;
    background: var(--backdrop);
  }
  .canvas { position: relative; width: 969px; height: 1200px; }
  .flyer {
    position: absolute; left: 183px; top: 187px;
    width: 624px; height: 866px;
    background: var(--paper);
    box-shadow: 0 6px 20px rgba(0,0,0,0.18);
  }
  .chalkboard {
    position: absolute; left: 40px; top: 39px;
    width: 546px; height: 346px;
    background: var(--board);
    border: 9px solid var(--board-frame);
    overflow: hidden;
  }
  .tutor-photo {
    position: absolute; right: 0; top: 6px;
    width: 180px; height: 322px;
    background: linear-gradient(180deg, #3d3d40 0%, #c9a98c 22%, #e6c9b0 35%, #1b1b1c 48%, #141414 100%);
    border-radius: 80px 80px 0 0;
  }
  .headline-list {
    position: absolute; left: 14px; top: 38px;
    list-style: none;
    font-family: "Cabin Sketch", cursive;
    font-weight: 700;
    font-size: 21px; line-height: 20px;
    text-transform: uppercase; letter-spacing: 1px;
  }
  .headline-list li { position: relative; padding-left: 16px; margin-bottom: 12px; }
  .headline-list li::before {
    content: ""; position: absolute; left: 0; top: 6px;
    width: 7px; height: 7px; background: currentColor;
  }
  .headline-pink { color: var(--chalk-pink); }
  .headline-blue { color: var(--chalk-blue); }
  .headline-green { color: var(--chalk-green); }
  .description {
    position: absolute; left: 41px; top: 396px; width: 544px;
    font-family: "Questrial", sans-serif;
    font-size: 16.4px; line-height: 21px;
    color: var(--ink);
    text-align: justify; text-align-last: center;
  }
  .offer-band {
    position: absolute; left: 42px; top: 489px;
    width: 541px; height: 65px;
    background: var(--offer-pink);
    color: var(--white);
    font-family: "Arvo", serif; font-weight: 700;
    font-size: 19.5px; line-height: 23px;
    text-transform: uppercase; text-align: center;
    display: flex; align-items: center; justify-content: center;
  }
  .contact-call {
    position: absolute; left: 0; top: 563px; width: 624px;
    font-family: "Questrial", sans-serif;
    font-size: 11.6px; text-transform: uppercase;
    color: var(--ink); text-align: center;
  }
  .brand-name {
    position: absolute; left: 0; top: 738px; width: 624px;
    font-family: "Questrial", sans-serif;
    font-size: 50px; line-height: 56px;
    color: var(--logo-ink); text-align: center;
  }
  .contact-footer {
    position: absolute; left: 0; bottom: 0;
    width: 624px; height: 58px;
    background: var(--footer-blue);
    color: var(--white);
    font-family: "Questrial", sans-serif;
  }
  .contact-row {
    display: flex; justify-content: center; align-items: center; gap: 8px;
    font-size: 15.5px;
  }
  .contact-row.primary { padding-top: 7px; gap: 8px; }
  .contact-row.secondary { font-size: 13.5px; padding-top: 4px; }
  .contact-item { display: inline-flex; align-items: center; gap: 7px; }
  .contact-row.primary .contact-item + .contact-item { margin-left: 6px; }
  .icon { width: 14px; height: 14px; flex: none; }
</style>
</head>
<body>
<div class="canvas">
  <article class="flyer">
    <section class="chalkboard">
      <ul class="headline-list">
        <li class="headline-pink">Feeling overwhelmed<br>by the HSC?</li>
        <li class="headline-blue">Looking to improve<br>your skills,<br>confidence<br>and organization?</li>
        <li class="headline-green">Want to increase your<br>child s engagement<br>at school?</li>
      </ul>
      <div class="tutor-photo" role="img" aria-label="Photo of a smiling tutor in glasses writing on the chalkboard"></div>
    </section>

    <p class="description">Lumivora Tutoring offers one-on-one, individualised learning experiences to maximise academic development. Our tutors are hand selected on the basis of their qualifications, expertise and passion for inspiring young learners.</p>

    <div class="offer-band">Mention this advertisement to claim<br>your trial session for just $10!</div>

    <p class="contact-call">Contact us today to discuss how we can help make your learning goals a reality!</p>

    <div class="brand-name">lumivora</div>

    <footer class="contact-footer">
      <div class="contact-row primary">
        <span class="contact-item">
          <svg class="icon" viewBox="0 0 14 14"><rect x="0.5" y="1.5" width="13" height="11" rx="2" fill="#fff"/><path d="M2.5 4.5 L7 8 L11.5 4.5" fill="none" stroke="#4a9fd8" stroke-width="1.3"/></svg>
          info@lumivoratutoring.com.au
        </span>
        <span class="contact-item">
          <svg class="icon" viewBox="0 0 14 14"><rect x="0.5" y="0.5" width="13" height="13" rx="2" fill="#fff"/><circle cx="7" cy="7" r="4.2" fill="none" stroke="#4a9fd8" stroke-width="1.1"/><path d="M2.8 7 H11.2 M7 2.8 C5 5 5 9 7 11.2 M7 2.8 C9 5 9 9 7 11.2" fill="none" stroke="#4a9fd8" stroke-width="0.9"/></svg>
          www/lumivoratutoring.com.au
        </span>
      </div>
      <div class="contact-row secondary">
        <span class="contact-item">
          <svg class="icon" viewBox="0 0 14 14"><rect x="0.5" y="0.5" width="13" height="13" rx="2" fill="#fff"/><path d="M7 11.5 C4.5 8.5 3.8 7 3.8 5.6 A3.2 3.2 0 0 1 10.2 5.6 C10.2 7 9.5 8.5 7 11.5 Z" fill="#4a9fd8"/><circle cx="7" cy="5.6" r="1.2" fill="#fff"/></svg>
          Suite 3, 88 Banksia Avenue Westbrook, Nsw 2000
        </span>
      </div>
    </footer>
  </article>
</div>
</body>
</html>
```